VORN - Business cards

Business card to be created for Commercial sales staff

Target Market(s)

Commercial businesses

Industry/Entity Type

Commercial

Contact Information for Business Card

Look professional. For commercial clients

Colors
ffffff

Requirements
Must have
• - Vorn Logo
• - Commercial sales staff as postion
• - room for commerical sales manager role
• - person name and their mobile number
• - Website : vornelectrical.com.au
Nice to have
• White background.
• On back of business card just have the logo no other information
Should not have
• Should only have white background on front of card.

```html
<!DOCTYPE html>
<html lang="en">
<head>
<meta charset="utf-8">
<title>VORN – Business Cards</title>
<link rel="stylesheet" href="https://fonts.googleapis.com/css2?family=Open+Sans:wght@400;700;800&display=swap">
<style>
  :root {
    --stage: #4b4b4d;
    --card-dark: #33363c;
    --card-light: #ffffff;
    --brand-red: #c4202a;
    --ink: #2b2d31;
  }
  * { margin: 0; padding: 0; box-sizing: border-box; }
  html, body { width: 1200px; height: 1200px; overflow: hidden; }
  body {
    background: var(--stage);
    font-family: "Open Sans", Arial, sans-serif;
    position: relative;
  }
  .card {
    position: absolute;
    left: 250px;
    width: 700px;
    height: 397px;
    border-radius: 20px;
    overflow: hidden;
  }
  .card-back { top: 170px; background: var(--card-dark); }
  .card-front { top: 634px; background: var(--card-light); }

  .wordmark {
    position: absolute;
    font-weight: 800;
    letter-spacing: 2px;
    line-height: 1;
    display: flex;
    align-items: center;
    gap: 16px;
  }
  .wordmark-dot {
    border-radius: 50%;
    background: var(--brand-red);
    flex: none;
  }
  .card-back .wordmark {
    color: var(--card-light);
    font-size: 104px;
    left: 0; right: 0; top: 142px;
    justify-content: center;
  }
  .card-back .wordmark-dot { width: 40px; height: 40px; }
  .card-front .wordmark {
    color: var(--card-dark);
    font-size: 78px;
    right: 40px; top: 50px;
  }
  .card-front .wordmark-dot { width: 30px; height: 30px; }

  .edge-art { position: absolute; left: 0; top: 0; }

  .identity {
    position: absolute;
    right: 382px;
    top: 266px;
    text-align: right;
  }
  .identity-name {
    color: var(--brand-red);
    font-weight: 700;
    font-size: 24px;
    line-height: 30px;
  }
  .identity-role {
    color: var(--ink);
    font-size: 17px;
    line-height: 24px;
  }
  .divider {
    position: absolute;
    left: 342px; top: 240px;
    width: 2px; height: 110px;
    background: var(--brand-red);
  }
  .contacts {
    position: absolute;
    left: 372px; top: 261px;
    list-style: none;
    color: var(--ink);
    font-size: 17px;
    line-height: 24px;
  }
  .contacts li { display: flex; align-items: center; gap: 9px; }
  .contacts svg { width: 14px; height: 14px; flex: none; }
</style>
</head>
<body>

  <section class="card card-back" aria-label="Card back">
    <div class="wordmark"><span class="wordmark-dot"></span>VORN</div>
  </section>

  <section class="card card-front" aria-label="Card front">
    <svg class="edge-art" width="700" height="397" viewBox="0 0 700 397" aria-hidden="true">
      <path d="M0 0 H40 C40 170 62 300 106 397 H0 Z" fill="var(--card-dark)"/>
      <path d="M40 122 C44 250 78 335 134 397 H120 C74 330 44 250 40 122 Z" fill="var(--brand-red)"/>
    </svg>

    <div class="wordmark"><span class="wordmark-dot"></span>VORN</div>

    <div class="identity">
      <p class="identity-name">Alex Smith</p>
      <p class="identity-role">Commercial sales staff</p>
    </div>

    <div class="divider"></div>

    <ul class="contacts">
      <li>
        <svg viewBox="0 0 14 14"><rect x="3.5" y="1" width="7" height="12" rx="1.5" fill="none" stroke="var(--brand-red)" stroke-width="1.5"/><circle cx="7" cy="10.8" r="0.8" fill="var(--brand-red)"/></svg>
        000-0000
      </li>
      <li>
        <svg viewBox="0 0 14 14"><rect x="1" y="3" width="12" height="8.5" fill="var(--brand-red)"/><path d="M1 3 L7 8 L13 3" fill="none" stroke="#fff" stroke-width="1.2"/></svg>
        asmith@vornelectrical.com.au
      </li>
      <li>
        <svg viewBox="0 0 14 14" fill="none" stroke="var(--brand-red)" stroke-width="1.1"><circle cx="7" cy="7" r="5.7"/><ellipse cx="7" cy="7" rx="2.5" ry="5.7"/><path d="M1.3 7 H12.7 M2.2 4 H11.8 M2.2 10 H11.8"/></svg>
        vornelectrical.com.au
      </li>
    </ul>
  </section>

</body>
</html>
```